New Writer Needs Website to Showcase Her Work

I'm a new writer of literary fiction. Several of my short stories have been published in literary journals, with more to come. I'm working on my first novel, and one of my stories will be featured in a "best of" anthology that will hit bookstores soon. I am not online at all at the moment (allergic to social media), but I would like readers, editors and agents to be able to find me if they like my work. Also, I'm told that editors and agents are more likely to take a chance with a writer who promotes her work online, hence my project. I've uploaded a few of my (very short) stories to give you the flavor of who I am as a writer. I write for adults, and my fiction has a dark edge to it. Not Harold Vance dark, not TBR dark, more like unhappy people trying to make their way in a world that demands happiness. If I were so lucky as to write a movie, I'd write a quirky, brooding, independent film, not a summer blockbuster. Think Winter at Cold Harbor, not Avalanche. Thank you for your help!

Target Market(s)

Literary editors, agents, publishers and readers.

Industry/Entity Type

Work

Logo Text

Clara Wynn Ashby

Number of Pages Required

1 page

Font styles to use
Serif
Sans Serif

Colors

Designer to choose colors to be used in the design.

Requirements
Must have
• Weight. I write serious stories, and I want that to come through. I will want to add links to my stories that are published online, notices for upcoming speaking engagements, publications, news, etc. I'll want a Bio section or page. I really don't know how many pages would be optimal, so I'm open to suggestions.
Nice to have
• Darker colors, but not anything obvious like black. Please resist the temptation to incorporate roses into your design.
Should not have
• Anything cute or fussy. I like clean lines, simple designs that draw you in with their beauty.

```html
<!DOCTYPE html>
<html lang="en">
<head>
<meta charset="utf-8">
<title>Clara Ashby — Literary Fiction</title>
<link rel="stylesheet" href="https://fonts.googleapis.com/css2?family=Open+Sans:ital,wght@0,300;0,400;0,600;0,700;0,800;1,300;1,400&display=swap">
<style>
:root{
  --ink:#1f2330;
  --muted:#6b6f78;
  --line:#e3e3e3;
  --navy:#2d3e55;
  --night:#0b0e2a;
  --press:#f5f5f5;
  --button:#0b0e2a;
  --white:#ffffff;
}
*{margin:0;padding:0;box-sizing:border-box}
html,body{width:1200px;height:3681px;overflow:hidden}
body{font-family:'Open Sans',Arial,sans-serif;color:var(--ink);background:var(--white);position:relative}
.abs{position:absolute}

/* header */
.site-header{position:absolute;left:0;top:0;width:1200px;height:98px;background:var(--white);border-bottom:1px solid var(--line)}
.logo{position:absolute;left:100px;top:30px;font-size:26px;font-weight:400;color:var(--ink)}
.main-nav{position:absolute;right:98px;top:40px;display:flex;gap:42px;font-size:14px}
.main-nav a{color:var(--ink);text-decoration:none}
.main-nav a.active{border-bottom:2px solid var(--ink);padding-bottom:10px}

/* hero */
.hero{position:absolute;left:0;top:98px;width:1200px;height:572px;background:linear-gradient(180deg,#2f2c33 0%,#3e3a3f 40%,#4a3a34 75%,#3a2a24 100%);text-align:center;color:var(--white)}
.hero h1{position:absolute;left:0;right:0;top:192px;font-size:52px;font-weight:800;letter-spacing:.5px}
.hero p{position:absolute;left:265px;width:670px;top:260px;font-size:15px;line-height:26px}
.hero .btn-primary{position:absolute;left:508px;top:339px;width:182px;height:51px;background:var(--button);color:var(--white);font-size:22px;line-height:51px}
.hero .arrow{position:absolute;top:270px}

/* section titles */
.section-title{position:absolute;left:100px;width:1000px;text-align:center;font-size:30px;font-weight:300;letter-spacing:1px}
.section-rule{position:absolute;left:100px;width:1000px;height:1px;background:var(--line)}

/* books */
.book{position:absolute;top:842px;width:233px;text-align:center}
.cover{width:233px;height:348px;border-radius:4px;position:relative;color:var(--white);box-shadow:0 2px 6px rgba(0,0,0,.25)}
.cover .title{position:absolute;top:22px;left:0;right:0;font-size:13px;font-weight:600}
.cover .author{position:absolute;top:76px;left:20px;right:20px;font-size:26px;font-weight:300;line-height:32px}
.book-rule{height:1px;background:var(--line);margin:42px -12px 0}
.book-byline{margin-top:18px;font-size:14px;font-style:italic;color:#444}
.btn-outline{display:inline-block;margin-top:26px;width:142px;height:42px;border:1px solid #555;font-size:14px;font-weight:600;line-height:40px;color:var(--ink)}

/* bio */
.bio{position:absolute;left:0;top:1436px;width:1200px;height:630px;background:var(--navy);color:var(--white)}
.bio .section-title{color:var(--white)}
.bio .section-rule{background:rgba(255,255,255,.2)}
.bio-photo{position:absolute;left:100px;top:194px;width:391px;height:345px;border:4px solid #8a93a3;background:linear-gradient(135deg,#d9d4cf,#b8ada6 60%,#8f8580)}
.bio-col{position:absolute;top:190px;font-size:12.5px;line-height:30px}

/* press */
.press{position:absolute;left:0;top:2066px;width:1200px;height:535px;background:var(--press)}
.quote{position:absolute;left:184px;width:834px;top:142px;text-align:center;font-size:14px;font-style:italic;font-weight:300;line-height:26px;color:#777}
.avatar{position:absolute;left:535px;top:290px;width:132px;height:132px;border-radius:50%;border:5px solid var(--white);background:linear-gradient(160deg,#cfc9bd,#8d857a);box-shadow:0 0 0 1px #ddd}
.cite{position:absolute;left:0;right:0;top:440px;text-align:center;font-size:16px;letter-spacing:1.5px;color:#555}

/* lower columns */
.col-heading{position:absolute;top:2674px;font-size:18px;font-weight:700}
.col-divider{position:absolute;top:2680px;width:1px;height:440px;background:var(--line)}
.small{font-size:12.5px;line-height:23px;color:#555}
.btn-view{position:absolute;left:103px;top:3065px;width:123px;height:40px;border:1px solid #333;font-size:16px;line-height:38px;padding-left:14px}
.news-item{position:absolute;left:483px;width:330px}
.date{position:absolute;left:0;top:0;width:108px;height:108px;border-radius:50%;border:1px solid #bbb;text-align:center}
.date b{display:block;font-size:44px;font-weight:300;margin-top:12px;line-height:52px}
.date span{font-size:11px;color:#555}
.news-text{position:absolute;left:130px;top:8px;width:200px}
.news-text h3{font-size:14px;font-weight:600;margin-bottom:6px}
.news-text p{font-size:12px;line-height:19px;color:#555}
.pub-img{position:absolute;left:876px;width:204px;height:111px;border:3px solid #ccc}
.pub-title{position:absolute;left:876px;font-size:13px;font-weight:600}
.pub-text{position:absolute;left:876px;width:210px;font-size:11.5px;line-height:18px;color:#555}

/* footer */
.site-footer{position:absolute;left:0;top:3190px;width:1200px;height:491px;background:var(--night);color:var(--white);text-align:center}
.footer-nav{position:absolute;left:0;right:0;top:86px;font-size:12px}
.footer-nav span{margin:0 12px}
.footer-nav i{font-style:normal;color:#667}
.subscribe{position:absolute;left:0;right:0;top:154px;font-size:24px;font-weight:400;letter-spacing:1px}
.subscribe-note{position:absolute;left:0;right:0;top:202px;font-size:11px;color:#cfd2dd}
.btn-signup{position:absolute;left:523px;top:243px;width:154px;height:50px;border:1px solid var(--white);font-size:20px;line-height:48px}
.social{position:absolute;top:325px;width:32px;height:32px;border-radius:50%;background:var(--white)}
.footer-rule{position:absolute;left:0;top:393px;width:1200px;height:1px;background:rgba(255,255,255,.12)}
.copyright{position:absolute;left:0;right:0;top:420px;font-size:12px;color:#cfd2dd}
</style>
</head>
<body>

<header class="site-header">
  <div class="logo">Clara Ashby</div>
  <nav class="main-nav">
    <a class="active">Home</a><a>Books</a><a>My Stories</a><a>Bio</a><a>Speaking Engagements</a><a>News</a><a>Contact</a>
  </nav>
</header>

<section class="hero" role="img" aria-label="Misty dark forest at dusk with autumn leaves">
  <svg class="arrow" style="left:34px" width="16" height="30" viewBox="0 0 16 30"><path d="M14 2 2 15l12 13" fill="none" stroke="#fff" stroke-opacity=".6" stroke-width="2"/></svg>
  <svg class="arrow" style="right:34px" width="16" height="30" viewBox="0 0 16 30"><path d="M2 2l12 13L2 28" fill="none" stroke="#fff" stroke-opacity=".6" stroke-width="2"/></svg>
  <h1>I'm a New Writer of Literary Fiction</h1>
  <p>Several of my short stories have been published in literary journals, with more to come. I'm working on my first novel, and one of my stories will be featured in a "best of" anthology that will hit bookstores soon.</p>
  <div class="btn-primary">My Stories</div>
</section>

<h2 class="section-title" style="top:724px">BOOKS</h2>
<div class="section-rule" style="top:780px"></div>

<article class="book" style="left:152px">
  <div class="cover" role="img" aria-label="Book cover: leaping figure over a large year numeral in rust tones" style="background:linear-gradient(160deg,#8a6a3a,#a4502e 60%,#7d3a22)">
    <div class="title">Fissure</div><div class="author">BY CLARA WYNN ASHBY</div>
  </div>
  <div class="book-rule"></div>
  <div class="book-byline">BY CLARA WYNN ASHBY</div>
  <div class="btn-outline">Learn More</div>
</article>
<article class="book" style="left:484px">
  <div class="cover" role="img" aria-label="Book cover: bare trees on a dark autumn field" style="background:linear-gradient(180deg,#2b2a26,#4f4a36 55%,#6c5d36)">
    <div class="title">Leftover Mud Pie</div><div class="author">BY CLARA WYNN ASHBY</div>
  </div>
  <div class="book-rule"></div>
  <div class="book-byline">BY CLARA WYNN ASHBY</div>
  <div class="btn-outline">Learn More</div>
</article>
<article class="book" style="left:816px">
  <div class="cover" role="img" aria-label="Book cover: two people on a bench, black and white" style="background:linear-gradient(180deg,#b9b9b9,#8d8d8d 60%,#666)">
    <div class="title">The Crossing</div><div class="author">BY CLARA WYNN ASHBY</div>
  </div>
  <div class="book-rule"></div>
  <div class="book-byline">BY CLARA WYNN ASHBY</div>
  <div class="btn-outline">Learn More</div>
</article>

<section class="bio">
  <h2 class="section-title" style="top:56px">BIO</h2>
  <div class="section-rule" style="top:115px"></div>
  <div class="bio-photo" role="img" aria-label="Hand writing with a pen on paper"></div>
  <p class="bio-col" style="left:545px;width:290px">On the other hand, we denounce with righteous indignation and dislike men who are so beguiled and demoralized by the charms of pleasure of the moment, so blinded by desire, that they cannot foresee the pain and trouble that are bound to ensue; and equal blame belongs to those who fail in their duty through weakness of will, which is the same as saying through shrinking from toil and pain. These cases are perfectly simple and easy to distinguish.</p>
  <p class="bio-col" style="left:874px;width:280px">In a free hour, when our power of choice is untrammelled and when nothing prevents our being able to do what we like best, every pleasure is to be welcomed and every pain avoided. But in certain circumstances and owing to the claims of duty or the obligations of business it will frequently occur that pleasures have to be repudiated and annoyances accepted. The wise man therefore always holds in these matters to this principle of selection.</p>
</section>

<section class="press">
  <h2 class="section-title" style="top:60px">IN THE PRESS</h2>
  <div class="section-rule" style="top:116px"></div>
  <svg class="abs" style="left:100px;top:208px" width="14" height="28" viewBox="0 0 14 28"><path d="M12 2 2 14l10 12" fill="none" stroke="#ccc" stroke-width="2"/></svg>
  <svg class="abs" style="left:1086px;top:208px" width="14" height="28" viewBox="0 0 14 28"><path d="M2 2l10 12L2 26" fill="none" stroke="#ccc" stroke-width="2"/></svg>
  <div class="abs" style="left:150px;top:118px;font-size:60px;color:#ddd;font-family:Georgia,serif">“</div>
  <div class="abs" style="left:1004px;top:230px;font-size:60px;color:#ddd;font-family:Georgia,serif">”</div>
  <p class="quote">But I must explain to you how all this mistaken idea of denouncing pleasure and praising pain was born and I will give you a complete account of the system, and expound the actual teachings of the great explorer of the truth, the master-builder of human happiness. No one rejects, dislikes, or avoids pleasure itself, because it is pleasure, but because those who do not know how to pursue pleasure rationally encounter consequences that are extremely painful</p>
  <div class="avatar" role="img" aria-label="Portrait of a traveller with a suitcase, seen from behind"></div>
  <div class="cite">– ASSUMENDA EST</div>
</section>

<h3 class="col-heading" style="left:100px">Upcoming Speaking Engagements</h3>
<div class="abs" role="img" aria-label="Open book beside a coffee cup near a window" style="left:100px;top:2736px;width:293px;height:172px;border:3px solid #ccc;background:linear-gradient(135deg,#d7dcc8,#b9a990 60%,#8e7e66)"></div>
<p class="abs small" style="left:100px;top:2928px;width:300px">Praesent a accumsan est. Nam ornare erat sed tortor iaculis posuere. Suspendisse tempus luctus nunc, ut laoreet leo. Nam neque tellus, ornare vitae lobortis id, sagittis vitae arcu. Maecenas a adipiscing nisl. Nullam sed risus sit amet ipsum lobortis condimentum.</p>
<div class="btn-view">View More ›</div>
<div class="col-divider" style="left:444px"></div>

<h3 class="col-heading" style="left:488px">News</h3>
<div class="news-item" style="top:2712px"><div class="date"><b>09</b><span>JAN / 2017</span></div><div class="news-text"><h3>NOSTRUD EXERCITATION</h3><p>Suspendisse tempus luctus nunc, ut laoreet leo. Nam neque tellus, ornare vitae lobortis.</p></div></div>
<div class="news-item" style="top:2849px"><div class="date"><b>04</b><span>FEB / 2017</span></div><div class="news-text"><h3>UNDE OMNIS ISTE NATUS</h3><p>Suspendisse tempus luctus nunc, ut laoreet leo. Nam neque tellus, ornare vitae lobortis.</p></div></div>
<div class="news-item" style="top:2989px"><div class="date"><b>15</b><span>JAN / 2017</span></div><div class="news-text"><h3>OFFICIA DESERUNT MOLLIT</h3><p>Suspendisse tempus luctus nunc, ut laoreet leo. Nam neque tellus, ornare vitae lobortis.</p></div></div>
<div class="col-divider" style="left:839px"></div>

<h3 class="col-heading" style="left:876px">Publications</h3>
<div class="pub-img" role="img" aria-label="Stack of open books on a table" style="top:2731px;background:linear-gradient(135deg,#e3d9c6,#b59c78)"></div>
<div class="pub-title" style="top:2852px">PRAESENT A ACCUMSAN EST</div>
<p class="pub-text" style="top:2872px">At vero eos et accusamus et iusto odio dignissimos ducimus qui blanditiis</p>
<div class="pub-img" role="img" aria-label="Silhouette celebrating behind a large year numeral at sunset" style="top:2935px;background:linear-gradient(180deg,#7ea6c9,#2e4a66 70%,#1d2a3a)"></div>
<div class="pub-title" style="top:3055px">MAURIS FERMENTUM MAGNA</div>
<p class="pub-text" style="top:3075px">Donec sit amet eros. Lorem ipsum dolor sit amet, consectetuer adipiscing elit.</p>

<footer class="site-footer">
  <div class="footer-nav"><span>Home</span><i>|</i><span>Books</span><i>|</i><span>My Stories</span><i>|</i><span>Bio</span><i>|</i><span>Speaking Engagements</span><i>|</i><span>News</span><i>|</i><span>Contact</span></div>
  <div class="subscribe">SUBSCRIBE YOUR NEWSLETTER</div>
  <div class="subscribe-note">sign up with your email address to receive news and updates.</div>
  <div class="btn-signup">SIGN UP</div>
  <div class="social" style="left:499px"></div>
  <div class="social" style="left:543px"></div>
  <div class="social" style="left:585px"></div>
  <div class="social" style="left:627px"></div>
  <div class="social" style="left:669px"></div>
  <div class="footer-rule"></div>
  <div class="copyright">© 2017 Clara Ashby . All rights reserved.</div>
</footer>

</body>
</html>
```